Quietly Orchard Honey Labels

We are an importer and distributor in the UK of fine foods from Spain. We sell primarily to the retail and wholesale trade. I need a design for wrap around labels to put on jars for four different varieties of honey - Creamy Spring Blossom, Lavender, Wild Forest and Wild Thyme. The honey originates from Spain and will primarily be sold online and to independent retailers. The look and feeling I am looking for is classical, traditional, artisan and natural. I am looking for something simple and not too fussy. There needs to be an immediate obvious distinction on each label between the 4 varieties of honey, ideally by the use of different colours in some way in each design, though I would prefer the label background to be predominantly white. It is not necessary in the design to make it evident that it is from Spain. I have attached images of the jars and the honeys and also an image of the current label just for reference (but do not refer to the design). I have also attached the text for each variety of honey. The measurements for the labels are as follows: 167mm wide and 82mm high. Our logo will go on top of the lid of the jar. I really like the design I have attached to my brief. It is labelled 'Honey Design'.

Target Market(s)

Independent food retailers and online consumers

Industry/Entity Type

Fine Foods

Font styles to use
Script
Other font styles liked:
• Freeland Font for the word Honey

Requirements
Must have
• It needs to be immediately obvious by sight that each of the 4 varieties of honey are different
Nice to have
• Just the one same icon on each label for each variety of honey. Simple. Not too fussy. I really like the design attached labelled 'honey font'.

```html
<!DOCTYPE html>
<html lang="en">
<head>
<meta charset="utf-8">
<title>Quietly Orchard – Lavender Honey Label</title>
<link rel="stylesheet" href="https://fonts.googleapis.com/css2?family=Abril+Fatface&display=swap">
<style>
  :root {
    --backdrop: #ece8e2;
    --label-white: #fbfbfb;
    --label-edge: #e6e6e6;
    --ink: #1c1c1c;
    --lavender-deep: rgba(122, 79, 176, 1);
    --lavender-mid: rgba(155, 115, 201, 0.85);
    --lavender-soft: rgba(205, 183, 230, 0.5);
    --lavender-clear: rgba(205, 183, 230, 0);
    --bee-amber: rgba(224, 162, 58, 0.6);
    --bee-clear: rgba(224, 162, 58, 0);
  }
  * { box-sizing: border-box; margin: 0; padding: 0; }
  html, body {
    width: 826px;
    height: 1200px;
    overflow: hidden;
    background: var(--backdrop);
  }
  .canvas {
    position: relative;
    width: 826px;
    height: 1200px;
  }
  .label {
    position: absolute;
    left: 63px;
    top: 230px;
    width: 700px;
    height: 740px;
    background: linear-gradient(90deg, #f1f1f1 0%, var(--label-white) 18%, var(--label-white) 78%, #ededed 100%);
    border: 1px solid var(--label-edge);
    overflow: hidden;
  }
  .art-lavender-corner {
    position: absolute;
    left: -60px;
    top: -60px;
    width: 380px;
    height: 360px;
    background: radial-gradient(ellipse closest-side at 50% 50%,
      var(--lavender-deep) 0%, var(--lavender-mid) 35%, var(--lavender-soft) 70%, var(--lavender-clear) 100%);
  }
  .art-bees-lavender {
    position: absolute;
    left: 250px;
    top: 400px;
    width: 520px;
    height: 440px;
    background:
      radial-gradient(ellipse 60px 42px at 74% 20%, var(--bee-amber) 0%, var(--bee-clear) 100%),
      radial-gradient(ellipse 55px 40px at 38% 38%, var(--bee-amber) 0%, var(--bee-clear) 100%),
      radial-gradient(ellipse closest-side at 52% 56%,
        var(--lavender-deep) 0%, var(--lavender-mid) 40%, var(--lavender-soft) 72%, var(--lavender-clear) 100%);
  }
  .brand {
    position: absolute;
    left: 0;
    right: 22px;
    top: 118px;
    display: flex;
    flex-direction: column;
    align-items: center;
    gap: 8px;
  }
  .brand-dot {
    width: 14px;
    height: 14px;
    border-radius: 50%;
    background: var(--ink);
  }
  .brand-name {
    font-family: "Abril Fatface", serif;
    font-size: 20px;
    line-height: 1.1;
    color: var(--ink);
    text-align: center;
  }
  .product-title {
    position: absolute;
    left: 0;
    right: 44px;
    top: 262px;
    font-family: "Abril Fatface", serif;
    font-size: 100px;
    font-weight: 400;
    line-height: 0.95;
    letter-spacing: 4px;
    color: var(--ink);
    text-align: center;
    text-transform: uppercase;
  }
</style>
</head>
<body>
  <div class="canvas">
    <section class="label">
      <div class="art-lavender-corner" role="img" aria-label="Watercolour lavender sprigs in the top left corner"></div>
      <div class="art-bees-lavender" role="img" aria-label="Watercolour bumblebees among lavender flowers"></div>
      <div class="brand">
        <span class="brand-dot"></span>
        <span class="brand-name">Quietly<br>Orchard</span>
      </div>
      <h1 class="product-title">Lavender<br>Honey</h1>
    </section>
  </div>
</body>
</html>
```